Korvane Sky Works, LLC - Business Card

I currently have a drone business that specializes in aerial photography, thermal image inspections, deer recovery, search and rescue, custom agricultural applications. i will attach my current business card as well as some logos to incorporate for a new up to date business card
Updates

Designs look the same

Sick

Target Market(s)

farmers, hunters

Contact Information for Business Card

name address phone number (as existing card i attached)

Requirements
Must have
• im good with existing business card, but would like an agricultural twist

```html
<!DOCTYPE html>
<html lang="en">
<head>
<meta charset="utf-8">
<title>Korvane Sky Works, LLC – Business Card</title>
<link rel="stylesheet" href="https://fonts.googleapis.com/css2?family=Montserrat:wght@400;500;600;700&display=swap">
<style>
  :root {
    --bg: #3a3a3a;
    --green: #5cb82a;
    --black: #0d0d0d;
    --card-dark: #1c1c1c;
    --white: #ffffff;
    --ink: #1a1a1a;
  }
  * { box-sizing: border-box; margin: 0; padding: 0; }
  html, body { width: 1200px; height: 1200px; overflow: hidden; }
  body {
    background: var(--bg);
    font-family: "Montserrat", sans-serif;
    display: flex;
    flex-direction: column;
    align-items: center;
    justify-content: center;
    gap: 44px;
  }
  .card {
    width: 900px;
    height: 514px;
    border-radius: 34px;
    position: relative;
    overflow: hidden;
    box-shadow: 0 14px 30px rgba(0,0,0,.45);
  }
  /* Front */
  .card-front { background: var(--white); color: var(--ink); }
  .front-band {
    position: absolute; left: 0; right: 0; bottom: 0; height: 54px;
    display: flex;
  }
  .front-band .band-green { flex: 0 0 66%; background: var(--green); }
  .front-band .band-black { flex: 1; background: var(--black); margin-left: 12px; margin-top: -28px; }
  .brand-mark {
    position: absolute; top: 70px; left: 520px;
    display: flex; align-items: center; gap: 14px;
  }
  .brand-mark .dot {
    width: 30px; height: 30px; border-radius: 50%; background: var(--green);
  }
  .brand-mark .brand-name {
    font-size: 44px; font-weight: 700; color: var(--ink); letter-spacing: 1px;
  }
  .services {
    position: absolute; top: 180px; left: 560px;
    list-style: none; font-size: 24px; font-weight: 600; line-height: 1.45;
  }
  .services li::before {
    content: "•"; color: var(--green); margin-right: 8px;
  }
  .contact-block { position: absolute; left: 70px; top: 200px; }
  .person-name { font-size: 38px; font-weight: 700; color: var(--green); letter-spacing: 1px; }
  .person-role { font-size: 22px; font-weight: 500; letter-spacing: 1px; margin-bottom: 16px; }
  .contact-list { list-style: none; font-size: 22px; line-height: 1.5; }
  .contact-list li { display: flex; align-items: flex-start; gap: 14px; }
  .contact-list svg { width: 24px; height: 24px; flex: 0 0 24px; margin-top: 5px; fill: var(--green); }
  .contact-list .addr { line-height: 1.25; }
  /* Back */
  .card-back { background: var(--card-dark); border-bottom: 6px solid var(--green); }
  .back-mark {
    position: absolute; inset: 0;
    display: flex; align-items: center; justify-content: center; gap: 22px;
  }
  .back-mark .ring {
    width: 56px; height: 56px; border-radius: 50%; border: 8px solid var(--green);
  }
  .back-mark .brand-name {
    font-size: 76px; font-weight: 700; color: var(--green); letter-spacing: 2px;
  }
</style>
</head>
<body>
  <section class="card card-front">
    <div class="brand-mark">
      <span class="dot"></span>
      <span class="brand-name">Korvane</span>
    </div>
    <ul class="services">
      <li>Thermal Image</li>
      <li>Deer Recovery</li>
      <li>Search &amp; Rescue</li>
      <li>Real Estate Photog</li>
    </ul>
    <div class="contact-block">
      <h1 class="person-name">MAREK HOLLOWAY</h1>
      <p class="person-role">OWNER</p>
      <ul class="contact-list">
        <li><svg viewBox="0 0 24 24"><path d="M6.6 10.8a15 15 0 0 0 6.6 6.6l2.2-2.2a1 1 0 0 1 1-.25 11.4 11.4 0 0 0 3.6.57 1 1 0 0 1 1 1V20a1 1 0 0 1-1 1A17 17 0 0 1 3 4a1 1 0 0 1 1-1h3.5a1 1 0 0 1 1 1c0 1.25.2 2.45.57 3.57a1 1 0 0 1-.25 1z"/></svg>555-014-2290</li>
        <li><svg viewBox="0 0 24 24"><path d="M2 5h20v14H2z M2 5l10 8 10-8" /></svg>korvanesky@mail.com</li>
        <li><svg viewBox="0 0 24 24"><path d="M12 2a10 10 0 1 0 0 20 10 10 0 0 0 0-20zm7.9 9h-3.4a15 15 0 0 0-1.4-6.1A8 8 0 0 1 19.9 11zM12 4c1 1.3 2.3 3.8 2.5 7h-5C9.7 7.8 11 5.3 12 4zM8.9 4.9A15 15 0 0 0 7.5 11H4.1a8 8 0 0 1 4.8-6.1zM4.1 13h3.4a15 15 0 0 0 1.4 6.1A8 8 0 0 1 4.1 13zM12 20c-1-1.3-2.3-3.8-2.5-7h5c-.2 3.2-1.5 5.7-2.5 7zm3.1-.9a15 15 0 0 0 1.4-6.1h3.4a8 8 0 0 1-4.8 6.1z"/></svg>www.korvaneskyworks.com</li>
        <li><svg viewBox="0 0 24 24"><path d="M12 2a7 7 0 0 0-7 7c0 5 7 13 7 13s7-8 7-13a7 7 0 0 0-7-7zm0 9.5A2.5 2.5 0 1 1 12 6.5a2.5 2.5 0 0 1 0 5z"/></svg><span class="addr">214 W. Orchard Rd.<br>Brenton, OH 40010</span></li>
      </ul>
    </div>
    <div class="front-band"><span class="band-green"></span><span class="band-black"></span></div>
  </section>

  <section class="card card-back">
    <div class="back-mark">
      <span class="ring"></span>
      <span class="brand-name">Korvane</span>
    </div>
  </section>
</body>
</html>
```